DM - management consultant

Business card - contemporary design

Front info
Dorian Maples

(Address not necessary)
PO Box 7386
Belmont, CA 94002

(650) 555-0143
dm@dorianmapl.es

Chirper: dmq527
Facetome: /Dorian.Maples
Linkwork: /in/dorianmaples

Back or Front
www.dorianmaples.net
Facilitation & coaching, change management, strategic partnerships, business improvement

Target Market(s)

High tech businesses - mostly startups in Silicon Valley

Industry/Entity Type

Business

Font styles to use
Sans Serif

Colors

Designer to choose colors to be used in the design.

```html
<!DOCTYPE html>
<html lang="en">
<head>
<meta charset="utf-8">
<title>Dorian Maples – Business Cards</title>
<link rel="stylesheet" href="https://fonts.googleapis.com/css2?family=Arimo:wght@400;700&family=Open+Sans:wght@400;600&display=swap">
<style>
  :root {
    --page: #eceae6;
    --navy-deep: #0f2c57;
    --navy: #1d4f8c;
    --blue-mid: #3a6fb0;
    --blue-soft: #8fb0dc;
    --ink: #1c1c1c;
    --ink-soft: #333a44;
    --rule: #2b5da8;
    --paper: #ffffff;
    --ghost: #e4e7f1;
  }
  * { box-sizing: border-box; margin: 0; padding: 0; }
  html, body { width: 1200px; height: 784px; overflow: hidden; }
  body {
    background: var(--page);
    font-family: "Open Sans", Arial, sans-serif;
    position: relative;
  }
  .card {
    position: absolute;
    top: 237px;
    width: 540px;
    height: 310px;
    overflow: hidden;
    box-shadow: 0 2px 8px rgba(0,0,0,0.15);
  }

  /* Back card */
  .card-back {
    left: 40px;
    background: linear-gradient(120deg, var(--navy-deep) 0%, var(--navy) 55%, var(--blue-mid) 100%);
    color: #fff;
  }
  .back-pattern {
    position: absolute;
    inset: 0;
    background:
      radial-gradient(ellipse at 100% 0%, rgba(143,176,220,0.55) 0%, rgba(143,176,220,0.2) 45%, rgba(143,176,220,0) 75%),
      linear-gradient(100deg, rgba(15,44,87,0.9) 0%, rgba(29,79,140,0.3) 60%, rgba(58,111,176,0.2) 100%);
  }
  .back-content {
    position: absolute;
    left: 150px;
    top: 22px;
    width: 300px;
    text-align: center;
  }
  .back-mark {
    display: inline-flex;
    align-items: center;
    gap: 8px;
    font-family: "Arimo", Arial, sans-serif;
    font-weight: 700;
    font-size: 34px;
    color: #fff;
    margin-bottom: 10px;
  }
  .back-mark .dot {
    width: 14px; height: 14px; border-radius: 50%;
    background: #fff;
  }
  .services {
    list-style: none;
    font-family: "Arimo", Arial, sans-serif;
    font-size: 12px;
    letter-spacing: 2.4px;
    text-transform: uppercase;
    line-height: 24px;
  }
  .web {
    position: absolute;
    left: 0; right: 0;
    bottom: 40px;
    text-align: center;
    font-family: "Arimo", Arial, sans-serif;
    font-size: 17px;
    letter-spacing: 4px;
  }

  /* Front card */
  .card-front {
    left: 620px;
    background: var(--paper);
  }
  .ghost-mark {
    position: absolute;
    right: 18px;
    top: 86px;
    font-family: "Arimo", Arial, sans-serif;
    font-weight: 700;
    font-size: 150px;
    line-height: 1;
    color: var(--ghost);
  }
  .front-mark {
    position: absolute;
    left: 40px;
    top: 62px;
    display: flex;
    align-items: center;
    gap: 10px;
    font-family: "Arimo", Arial, sans-serif;
    font-weight: 700;
    font-size: 64px;
    line-height: 1;
    color: var(--navy);
  }
  .front-mark .dot {
    width: 18px; height: 18px; border-radius: 50%;
    background: var(--navy);
  }
  .identity {
    position: absolute;
    left: 222px;
    top: 56px;
  }
  .identity .name {
    font-family: "Arimo", Arial, sans-serif;
    font-weight: 700;
    font-size: 29px;
    color: var(--ink);
    padding-bottom: 3px;
    border-bottom: 2px solid var(--rule);
  }
  .identity .role {
    font-family: "Arimo", Arial, sans-serif;
    font-size: 9.5px;
    letter-spacing: 3.2px;
    text-transform: uppercase;
    color: var(--ink);
    margin-top: 5px;
  }
  .contacts {
    position: absolute;
    left: 32px;
    bottom: 26px;
    list-style: none;
    font-size: 15px;
    color: var(--ink-soft);
    line-height: 21px;
  }
  .contacts li { display: flex; align-items: center; gap: 6px; }
  .contacts .gap { margin-top: 12px; }
  .icon { width: 15px; height: 15px; flex: none; }
  .social-square {
    width: 14px; height: 14px; flex: none;
    background: var(--blue-mid);
    border-radius: 2px;
  }
</style>
</head>
<body>

  <section class="card card-back" aria-label="Business card back">
    <div class="back-pattern" role="img" aria-label="Blue field of receding soft circles"></div>
    <div class="back-content">
      <div class="back-mark"><span class="dot"></span>DM</div>
      <ul class="services">
        <li>Facilitation &amp; coaching</li>
        <li>Change management</li>
        <li>Strategic partnerships</li>
        <li>Business improvement</li>
      </ul>
    </div>
    <div class="web">www.dorianmaples.net</div>
  </section>

  <section class="card card-front" aria-label="Business card front">
    <div class="ghost-mark" aria-hidden="true">DM</div>
    <div class="front-mark"><span class="dot"></span>DM</div>
    <div class="identity">
      <div class="name">Dorian Maples</div>
      <div class="role">Management Consultant</div>
    </div>
    <ul class="contacts">
      <li>
        <svg class="icon" viewBox="0 0 16 16" aria-hidden="true"><path fill="#2b5da8" d="M3.6 1.5l2.3 2.6-1.3 1.6c.9 2 2.5 3.6 4.6 4.6l1.6-1.3 2.6 2.3-1.3 2.2C7.5 13.2 2.8 8.5 1.4 2.8z"/></svg>
        (650) 555-0143
      </li>
      <li>
        <svg class="icon" viewBox="0 0 16 16" aria-hidden="true"><rect x="1.5" y="3.5" width="13" height="9" fill="none" stroke="#2b5da8" stroke-width="1.6"/><path d="M1.5 3.5l6.5 5 6.5-5" fill="none" stroke="#2b5da8" stroke-width="1.6"/></svg>
        dm@dorianmapl.es
      </li>
      <li class="gap"><span class="social-square"></span>Chirper: dmq527</li>
      <li><span class="social-square"></span>Facetome: /Dorian.Maples</li>
      <li><span class="social-square"></span>Linkwork: /in/dorianmaples</li>
    </ul>
  </section>

</body>
</html>
```